a4 size poster for theatre school

I am looking for an eye catching poster for my theatre school - Bright Lantern Stage school - View our website here for the style we have already www.brightlanternstage.co.uk

Wording needs to include;

* Award Winning, Accredited, Affordable Performing Arts Classes taught by Leading Industry Experts

* Ages 4- 21 years

* All classes contain all three disciplines of Drama, Singing & Dance keeping cost low and enjoyment high

* Classes offered;
Drama
PQVR
Singing
KSBU dance
Freestyle Ballet
Freestyle Tap
Contemporary
Street
Jazz Musical Theatre

* FREE casting agency for TV and Theatre Available. Ten pupils currently performing in West End Productions, 8 pupils currently on screen in TV commercials, several pupils currently working on film & TV projects for Zorbiville, Quellmark Plus & Vista 9.

* Optional KSBU and PQVR exams

* Unparalleled performance opportunities both locally and in the West End

Our quality training is evident in our pupils success

* Now in our successful 17th Year!

* Awarded recognition from the Board for Stagecraft, Voice and Movement Studies - The industry regulator for children's performing arts training.

Target Market(s)

Parents & Children ages 4-21 years

Industry/Entity Type

Performing arts

Font styles to use
Other font styles liked:
• Arvo

Colors
EB3D1F
EC4F4E
F09395
F8D3D4
FCEDEE
6B429C
8869AF
B7A5CE
E3DAEB
F3F0F8

Requirements
Must have
• A good mix of photo's pf boys & girls. Different ethnicities. Different ages
Nice to have
• Wording very clear
Should not have
• Too many words

```html
<!DOCTYPE html>
<html lang="en">
<head>
<meta charset="utf-8">
<title>Bright Lantern Stage school – Poster</title>
<link rel="stylesheet" href="https://fonts.googleapis.com/css2?family=Barlow:wght@600;700&family=Raleway:wght@500;600&display=swap">
<style>
  :root {
    --page: #ffffff;
    --night: #07070c;
    --stage-blue: #1b2a8a;
    --stage-violet: #4a2a7a;
    --stage-red: #8a1f3a;
    --red: #e0383c;
    --red-panel: rgba(226, 58, 62, 0.9);
    --yellow: #fff200;
    --tick: #f4d400;
    --white: #ffffff;
    --pill-dark: rgba(30, 26, 30, 0.85);
  }
  * { box-sizing: border-box; margin: 0; padding: 0; }
  html, body { width: 1200px; height: 1000px; overflow: hidden; background: var(--page); }
  body { position: relative; font-family: "Barlow", Arial, sans-serif; }

  .poster {
    position: absolute; left: 298px; top: 73px; width: 604px; height: 854px;
    background: var(--night); overflow: hidden; color: var(--white); text-align: center;
  }
  .stage-photo {
    position: absolute; inset: 0;
    background:
      radial-gradient(ellipse 60% 40% at 25% 22%, rgba(70, 90, 220, 0.75), transparent 70%),
      radial-gradient(ellipse 55% 40% at 80% 30%, rgba(120, 60, 170, 0.7), transparent 70%),
      radial-gradient(ellipse 45% 30% at 70% 55%, rgba(160, 40, 70, 0.55), transparent 70%),
      linear-gradient(180deg, var(--stage-blue) 0%, var(--stage-violet) 35%, #2a1530 60%, var(--night) 88%);
  }
  .light-band {
    position: absolute; left: 0; right: 0; top: 377px; height: 22px;
    background: rgba(255, 255, 255, 0.12);
  }

  .brand {
    position: absolute; left: 0; right: 0; top: 190px;
    display: flex; align-items: center; justify-content: center; gap: 12px;
  }
  .brand-dot { width: 34px; height: 34px; border-radius: 50%; background: var(--yellow); }
  .brand-name { font-family: "Barlow", Arial, sans-serif; font-weight: 700; font-size: 34px; color: var(--yellow); line-height: 1.05; }

  .tagline {
    position: absolute; left: 76px; width: 452px; top: 317px;
    background: var(--pill-dark); border-radius: 14px; padding: 3px 6px;
    color: var(--yellow); font-weight: 700; font-size: 16.5px; line-height: 23px;
  }
  .ages {
    position: absolute; left: 191px; width: 222px; top: 379px; height: 37px;
    background: var(--red); border-radius: 19px;
    font-weight: 700; font-size: 23px; line-height: 37px;
  }
  .intro {
    position: absolute; left: 20px; right: 20px; top: 425px;
    font-weight: 700; font-size: 20.5px; line-height: 29px;
  }

  .panel {
    position: absolute; top: 497px; height: 157px;
    background: var(--red-panel); border-radius: 10px;
  }
  .classes { left: 34px; width: 256px; }
  .casting { left: 302px; width: 264px; text-align: left; padding: 24px 10px 0 12px;
    font-family: "Raleway", Arial, sans-serif; font-weight: 600; font-size: 11.6px; line-height: 17px; }
  .classes-title { margin-top: 7px; color: var(--yellow); font-weight: 700; font-size: 18.5px; line-height: 22px; }
  .class-cols { position: absolute; left: 12px; top: 31px; right: 8px; display: flex; }
  .class-list { list-style: none; text-align: left; font-weight: 700; font-size: 12.5px; }
  .class-list li { position: relative; padding-left: 17px; height: 26px; line-height: 14px; }
  .class-list li::before {
    content: ""; position: absolute; left: 0; top: 3px; width: 8px; height: 8px;
    border-radius: 50%; background: var(--tick);
  }
  .col-a { width: 115px; padding-top: 0; }
  .col-b { padding-left: 12px; border-left: 2px solid var(--yellow); margin-top: -2px; }
  .col-b li.two-line { height: 46px; }
  .col-b li.gap { height: 30px; }

  .highlights {
    position: absolute; left: 10px; right: 10px; top: 673px;
    font-weight: 700; font-size: 15.5px; line-height: 29px;
  }
  .highlights .gold { color: var(--yellow); }
  .highlights .closing { line-height: 23px; margin-top: 0; }
</style>
</head>
<body>
  <main class="poster">
    <div class="stage-photo" role="img" aria-label="Collage of stage photographs of young performers of different ages dancing and singing under blue and purple stage lights"></div>
    <div class="light-band"></div>

    <div class="brand">
      <span class="brand-dot"></span>
      <span class="brand-name">Bright Lantern<br>Stage school</span>
    </div>

    <p class="tagline">Award Winning, Accredited, Affordable Performing Arts<br>Classes taught by Leading Industry Experts</p>
    <p class="ages">AGES 4- 21 YEARS</p>
    <p class="intro">All classes contain all three disciplines of Drama,<br>Singing &amp; Dance keeping cost low and enjoyment high</p>

    <section class="panel classes">
      <h2 class="classes-title">CLASSES OFFERED:</h2>
      <div class="class-cols">
        <ul class="class-list col-a">
          <li>Drama</li>
          <li>Freestyle Tap</li>
          <li>Street</li>
          <li>Singing</li>
          <li>Contemporary</li>
        </ul>
        <ul class="class-list col-b">
          <li class="two-line">Jazz Musical<br>Theatre</li>
          <li class="gap">KSBU dance</li>
          <li class="gap">PQVR</li>
          <li>Freestyle Ballet</li>
        </ul>
      </div>
    </section>

    <section class="panel casting">
      <p>FREE casting agency for TV and Theatre Available. Ten pupils currently performing in West End Productions, 8 pupils currently on screen in TV commercials, several pupils currently working on film &amp; TV projects for Zorbiville, Quellmark Plus &amp; Vista 9.</p>
    </section>

    <div class="highlights">
      <p class="gold">Optional KSBU and PQVR exams</p>
      <p>Unparalleled performance opportunities both locally and in the West End</p>
      <p class="gold">Our quality training is evident in our pupils success</p>
      <p class="gold">Now in our successful 17th Year!</p>
      <p class="closing">Awarded recognition from the Board for Stagecraft, Voice and Movement Studies -<br>The industry regulator for children's performing arts training.</p>
    </div>
  </main>
</body>
</html>
```